Tactical Supply Company needing memorable business card design

Our tactical supply comapny is in need of a new business card design that will set us apart from the amateurs. We sell tactical gear ranging from backpacks and range bags to apparel and other gear. We are looking for a sharp design that incorporates our logo, website, and name. Our colors are white, red, and black, or any combination of the three, preferably red and black.
I have attached our logo with our name underneath but I have also edited that design with the logo incorporated next to the name (attached).

Target Market(s)

Law enforcement, military, tactical

Industry/Entity Type

Business

Contact Information for Business Card

Include www.fernhollowprovisions-demo.com

Colors
000000
ec1f27
ffffff

Requirements
Must have
• Our name, logo, and website. This is intended to be a memorable simple card, no name, address, email, or phone number info is necessary. Designs that do include this additional info will still be considered if they are absolutely spectacular.
Should not have
• A standard template design, I can create that in my own on Cardvellum. I am looking for a new, creative design that is completely unique to my company.

```html
<!DOCTYPE html>
<html lang="en">
<head>
<meta charset="utf-8">
<title>Fernhollow Provisions – Business Card</title>
<link rel="stylesheet" href="https://fonts.googleapis.com/css2?family=Quicksand:wght@400;500&display=swap">
<style>
  :root {
    --page-bg: #2a2a2a;
    --red-deep: #6e0a0d;
    --red-main: #8f1014;
    --red-bright: #ec1f27;
    --red-soft: #a8222a;
    --text-light: #f3dede;
    --text-muted: #c79a9c;
    --icon-grey: #8d7d7e;
  }
  * { box-sizing: border-box; margin: 0; padding: 0; }
  html, body { width: 1200px; height: 900px; overflow: hidden; }
  body {
    background: var(--page-bg);
    font-family: "Quicksand", sans-serif;
    position: relative;
  }
  .card {
    position: absolute;
    left: 250px;
    width: 700px;
    height: 400px;
    overflow: hidden;
    box-shadow: 0 10px 30px rgba(0,0,0,.5);
  }
  .card--back {
    top: 30px;
    background: linear-gradient(120deg, #7a4446 0%, #7a2226 35%, var(--red-deep) 75%, #5e0a0c 100%);
  }
  .card--front {
    top: 470px;
    background: linear-gradient(115deg, var(--red-deep) 0%, #9a181c 40%, var(--red-main) 70%, #7a0b0e 100%);
  }
  .brand {
    position: absolute;
    right: 120px;
    top: 150px;
    text-align: right;
  }
  .brand__name {
    font-size: 30px;
    font-weight: 500;
    color: var(--text-light);
    letter-spacing: .5px;
  }
  .brand__rule {
    height: 1px;
    width: 360px;
    background: var(--red-bright);
    margin: 6px 0 10px auto;
  }
  .brand__site {
    font-size: 18px;
    color: var(--text-muted);
  }
  .person {
    position: absolute;
    left: 40px;
    top: 150px;
  }
  .person__name {
    font-size: 28px;
    color: var(--text-light);
  }
  .person__role {
    font-size: 20px;
    color: var(--text-muted);
    margin-top: 14px;
  }
  .divider {
    position: absolute;
    left: 330px;
    top: 60px;
    width: 1px;
    height: 290px;
    background: var(--red-bright);
  }
  .contacts {
    position: absolute;
    left: 350px;
    top: 90px;
    list-style: none;
  }
  .contacts li {
    display: flex;
    align-items: center;
    gap: 12px;
    font-size: 20px;
    color: var(--text-light);
    height: 34px;
  }
  .contacts .gap { height: 70px; }
  .contacts svg { width: 18px; height: 18px; fill: var(--icon-grey); flex: none; }
  .edge-band {
    position: absolute;
    right: 0;
    top: 0;
    width: 70px;
    height: 100%;
    background: linear-gradient(90deg, var(--red-soft), #b5262d);
    box-shadow: -4px 0 10px rgba(0,0,0,.3);
  }
</style>
</head>
<body>
  <section class="card card--back">
    <div class="brand">
      <p class="brand__name">Fernhollow Provisions</p>
      <div class="brand__rule"></div>
      <p class="brand__site">www.fernhollowprovisions-demo.com</p>
    </div>
  </section>

  <section class="card card--front">
    <div class="person">
      <p class="person__name">Your Name</p>
      <p class="person__role">Your profesion</p>
    </div>
    <div class="divider"></div>
    <ul class="contacts">
      <li><svg viewBox="0 0 24 24"><path d="M6.6 10.8a15 15 0 0 0 6.6 6.6l2.2-2.2a1 1 0 0 1 1-.25 11.4 11.4 0 0 0 3.6.57 1 1 0 0 1 1 1V20a1 1 0 0 1-1 1A17 17 0 0 1 3 4a1 1 0 0 1 1-1h3.5a1 1 0 0 1 1 1c0 1.25.2 2.45.57 3.57a1 1 0 0 1-.25 1z"/></svg>0034.555.014</li>
      <li><svg viewBox="0 0 24 24"><path d="M2 5h20v14H2zm2 2v.4l8 5.2 8-5.2V7zm16 10V9.8l-8 5.2-8-5.2V17z"/></svg>yourmail@example.com</li>
      <li class="gap"></li>
      <li><svg viewBox="0 0 24 24"><path d="M12 2a10 10 0 1 0 0 20 10 10 0 0 0 0-20zm6.9 6h-3a15 15 0 0 0-1.3-3.9A8 8 0 0 1 18.9 8zM12 4c.8 1.2 1.5 2.5 1.9 4h-3.8c.4-1.5 1.1-2.8 1.9-4zM4.3 14a8 8 0 0 1 0-4h3.4a16 16 0 0 0 0 4zm.8 2h3a15 15 0 0 0 1.3 3.9A8 8 0 0 1 5.1 16zM8 8H5.1a8 8 0 0 1 4.3-3.9A15 15 0 0 0 8 8zm4 12c-.8-1.2-1.5-2.5-1.9-4h3.8c-.4 1.5-1.1 2.8-1.9 4zm2.3-6H9.7a14 14 0 0 1 0-4h4.6a14 14 0 0 1 0 4zm.3 5.9A15 15 0 0 0 16 16h3a8 8 0 0 1-4.4 3.9zM16.3 14a16 16 0 0 0 0-4h3.4a8 8 0 0 1 0 4z"/></svg>www.fernhollowprovisions-demo.com</li>
      <li><svg viewBox="0 0 24 24"><path d="M12 2a7 7 0 0 0-7 7c0 5.2 7 13 7 13s7-7.8 7-13a7 7 0 0 0-7-7zm0 9.5A2.5 2.5 0 1 1 12 6.5a2.5 2.5 0 0 1 0 5z"/></svg>yourstreet</li>
    </ul>
    <div class="edge-band"></div>
  </section>
</body>
</html>
```